Computer Service Provider in Need of New Letterhead Design

We are Larkvale Computer Services, a computer/IT services company that provides IT Support, software, hardware, virus monitoring, etc. in Vermont. We are looking for new letterhead, that is both professional and matches the current theme of our business cards & website.
Please note that we want to include the following information:
www.Larkvale.example
802-555-0147
47 Fernwick Hollow Road, Williston, VT 05495
Proactive Solutions • Approachable People • Proven Performance
I will be attaching our logo along with the business card images.
We would love to have the

```html
<!DOCTYPE html>
<html lang="en">
<head>
<meta charset="utf-8">
<title>Larkvale Computer Services — Letterhead</title>
<link href="https://fonts.googleapis.com/css2?family=Open+Sans:wght@400;600;700;800&display=swap" rel="stylesheet">
<style>
  :root {
    --navy: #1c3f78;
    --gold: #f7c520;
    --gold-soft: #ffe48a;
    --tag-gold: #ffd84a;
    --ink: #2b2b2b;
    --paper: #ffffff;
  }
  html, body {
    margin: 0;
    padding: 0;
    overflow: hidden;
    background: var(--paper);
  }
  .letterhead {
    position: relative;
    width: 849px;
    height: 1200px;
    overflow: hidden;
    background: var(--paper);
    font-family: "Open Sans", Arial, sans-serif;
    color: var(--ink);
  }
  .shapes {
    position: absolute;
    inset: 0;
    width: 849px;
    height: 1200px;
  }
  .taglines {
    position: absolute;
    left: 22px;
    top: 10px;
    margin: 0;
    padding: 0;
    list-style: none;
    color: var(--tag-gold);
    font-size: 18px;
    font-weight: 600;
    line-height: 38px;
    letter-spacing: 0.3px;
  }
  .brand {
    position: absolute;
    right: 30px;
    top: 192px;
    width: 310px;
    text-align: center;
    color: var(--navy);
    font-weight: 700;
  }
  .brand-name {
    display: block;
    font-size: 58px;
    line-height: 62px;
    letter-spacing: -0.5px;
  }
  .brand-sub {
    display: block;
    font-size: 22px;
    line-height: 28px;
    letter-spacing: 3.2px;
    text-transform: uppercase;
  }
  .letter {
    position: absolute;
    left: 62px;
    top: 390px;
    width: 730px;
    font-size: 15.5px;
    line-height: 25px;
  }
  .salutation {
    margin: 0 0 35px;
    font-weight: 700;
    font-size: 16px;
  }
  .body-copy {
    margin: 0 0 25px;
  }
  .signoff {
    margin: 60px 0 0;
    font-weight: 700;
    font-size: 16px;
    line-height: 28px;
  }
  .closing {
    display: block;
    margin-bottom: 22px;
  }
  .contact {
    position: absolute;
    left: 0;
    right: 0;
    top: 998px;
    text-align: center;
    color: var(--navy);
    font-style: normal;
    font-weight: 700;
    font-size: 13px;
    line-height: 20px;
    letter-spacing: 1.2px;
  }
  .website {
    position: absolute;
    left: 0;
    right: 0;
    top: 1140px;
    text-align: center;
    color: var(--gold);
    font-weight: 700;
    font-size: 24px;
    letter-spacing: 0.5px;
  }
</style>
</head>
<body>
<div class="letterhead">
  <svg class="shapes" viewBox="0 0 849 1200" aria-hidden="true">
    <polygon points="0,168 470,168 452,128 0,128" fill="var(--gold)"/>
    <polygon points="0,0 598,0 552,128 0,128" fill="var(--navy)"/>
    <polygon points="0,1040 849,978 849,1000 0,1060" fill="var(--gold-soft)"/>
    <polygon points="0,1060 849,1000 849,1118 0,1118" fill="var(--gold)"/>
    <polygon points="0,1118 849,1092 849,1200 0,1200" fill="var(--navy)"/>
  </svg>

  <ul class="taglines">
    <li>• Proactive Solutions •</li>
    <li>• Approachable People •</li>
    <li>• Proven Performance •</li>
  </ul>

  <div class="brand" aria-label="Larkvale Computer Services">
    <span class="brand-name">Larkvale</span>
    <span class="brand-sub">Computer Services</span>
  </div>

  <main class="letter">
    <p class="salutation">Dear Mr. Hale,</p>
    <p class="body-copy">A letterhead is the heading at the top of a sheet of letter paper (stationery). That heading usually consists of a name and an address, and a logo or corporate design, and sometimes a background pattern.</p>
    <p class="body-copy">The term "letterhead" is often used to refer to the whole sheet imprinted with such a heading. Many companies and individuals prefer to create a letterhead template in a word processor or other software application. This generally includes the same information as pre-printed stationery but without the additional costs involved. Letterhead can then be printed on stationery (or plain paper) as needed on a local output device or sent electronically.</p>
    <p class="body-copy">That heading usually consists of a name and an address, and a logo or corporate design, and sometimes a background pattern. The term "letterhead" is often used to refer to the whole sheet imprinted with such a heading.</p>
    <p class="signoff">
      <span class="closing">Sincerely,</span>
      Nora Pellett<br>
      Head of Accounts
    </p>
  </main>

  <address class="contact">
    802-555-0147<br>
    47 Fernwick Hollow Road, Maplecrest, EV 00817
  </address>

  <div class="website">www.Larkvale.example</div>
</div>
</body>
</html>
```